Stationery design for BrookSpan
Letterhead, Business card and envelope
Project: Stationery design for BrookSpan
Stationery design for BrookSpan -
Creative Brief
Simple
Name Surname
Director, Fixed Income & Currencies Trading
BrookSpan Associates Limited Harbor Court 17, Oduya Close City, Region, Country
Dayo@brook-span.example
RC 482316
For Letterhead and Envelope, Details are; BrookSpan Associates Limited Harbor Court, 17, Oduya Close City, Region, Country contact@brook-span.example +234 (1) 5558214

```html
<!DOCTYPE html>
<html lang="en">
<head>
<meta charset="utf-8">
<title>BrookSpan Stationery Concepts</title>
<link href="https://fonts.googleapis.com/css2?family=Cinzel:wght@400;600&family=Open+Sans:wght@400;600&display=swap" rel="stylesheet">
<style>
  :root{
    --backdrop:#e8dcc7;
    --paper:#ffffff;
    --ink:#111111;
    --ink-soft:#555555;
    --brand-red:#8e2a22;
    --brand-red-light:#b8473c;
    --label:#6b5f50;
    --placeholder-grey:#e3e3e3;
    --placeholder-pink:#f1e2e0;
  }
  *{box-sizing:border-box;margin:0;padding:0}
  html,body{width:1200px;height:446px;overflow:hidden}
  body{background:var(--backdrop);position:relative;font-family:"Open Sans",Arial,sans-serif;color:var(--ink)}
  .label{position:absolute;font-family:"Cinzel",Georgia,serif;font-size:7px;letter-spacing:1.5px;text-transform:uppercase;color:var(--label);white-space:nowrap}
  .sheet{position:absolute;background:var(--paper);box-shadow:0 2px 5px rgba(0,0,0,.22);overflow:hidden}
  .top-band{position:absolute;left:0;top:0;right:0;background:var(--ink);border-bottom:solid var(--brand-red)}
  .wordmark{position:absolute;display:flex;align-items:center;gap:4px;font-family:"Cinzel",Georgia,serif;font-weight:400;color:var(--ink);letter-spacing:.5px;white-space:nowrap}
  .wordmark .mark{background:var(--brand-red)}
  .fineprint{position:absolute;font-size:3.2px;line-height:1.5;color:var(--ink-soft)}
  .badge{position:absolute;border-radius:2px}
  .badge.grey{background:linear-gradient(var(--placeholder-grey),#f4f4f4)}
  .badge.pink{background:linear-gradient(var(--placeholder-pink),#f8f0ef)}

  /* business cards */
  .card-front{left:19px;top:151px;width:144px;height:87px}
  .card-front .top-band{height:6px;border-bottom-width:1.5px}
  .card-front .wordmark{right:8px;top:18px;font-size:8px}
  .card-front .wordmark .mark{width:6px;height:6px}
  .card-front .person{position:absolute;left:8px;top:44px;font-size:3.6px;line-height:1.5;color:var(--ink-soft)}
  .card-front .person strong{display:block;font-size:4.4px;color:var(--ink)}
  .card-front .contact{position:absolute;right:8px;top:56px;font-size:3.4px;line-height:1.5;text-align:right;color:var(--ink-soft)}
  .card-back{left:19px;top:259px;width:144px;height:64px;display:flex;align-items:center;justify-content:center}
  .card-back .wordmark{position:static;font-size:7px}
  .card-back .wordmark .mark{width:10px;height:6px}

  /* letterheads */
  .letterhead-one{left:187px;top:19px;width:259px;height:400px}
  .letterhead-two{left:473px;top:19px;width:300px;height:400px}
  .letterhead-one .top-band,.letterhead-two .top-band{height:10px;border-bottom-width:2.5px}
  .letterhead-one .wordmark,.letterhead-two .wordmark{right:26px;top:30px;font-size:10px}
  .letterhead-one .wordmark .mark,.letterhead-two .wordmark .mark{width:8px;height:8px}

  /* envelopes */
  .envelope-dark{left:804px;top:19px;width:382px;height:118px;background:var(--ink);border-radius:0 0 60px 60px/0 0 34px 34px}
  .envelope-red{left:804px;top:144px;width:382px;height:77px;background:radial-gradient(ellipse at 50% 40%,var(--brand-red-light),var(--brand-red) 70%);border-radius:0 0 60px 60px/0 0 30px 30px}
  .envelope-flap{left:804px;top:228px;width:382px;height:64px;border-radius:0 0 60px 60px/0 0 30px 30px}
  .envelope-flap .wordmark{left:212px;top:28px;font-size:8px}
  .envelope-flap .wordmark .mark{width:7px;height:7px}
  .envelope-front{left:794px;top:262px;width:204px;height:150px}
  .envelope-front .top-band{height:8px;border-bottom-width:2px}
  .envelope-front .wordmark{left:22px;top:44px;font-size:9px}
  .envelope-front .wordmark .mark{width:7px;height:7px}
</style>
</head>
<body>
  <p class="label" style="left:16px;top:96px">Stationery Concepts</p>

  <section class="sheet card-front">
    <div class="top-band"></div>
    <div class="wordmark"><span class="mark"></span>BrookSpan</div>
    <div class="person"><strong>Name Surname</strong>Director, Fixed Income<br>&amp; Currencies Trading</div>
    <div class="contact">name@company.example<br>RC 000000</div>
  </section>
  <p class="label" style="left:19px;top:244px">Business Card Front</p>

  <section class="sheet card-back">
    <div class="wordmark"><span class="mark"></span>BrookSpan</div>
  </section>
  <p class="label" style="left:19px;top:330px">Business Card Back</p>

  <section class="sheet letterhead-one">
    <div class="top-band"></div>
    <div class="wordmark"><span class="mark"></span>BrookSpan</div>
    <p class="fineprint" style="left:82px;top:340px">Company Name Limited<br>Street Address Line<br>City, Region, Country<br>mail@company.example<br>+000 (0) 0000000</p>
    <div class="badge grey" style="left:140px;top:346px;width:40px;height:30px"></div>
    <div class="badge pink" style="left:190px;top:346px;width:40px;height:30px"></div>
  </section>
  <p class="label" style="left:275px;top:427px">Letter Head Option 1</p>

  <section class="sheet letterhead-two">
    <div class="top-band"></div>
    <div class="wordmark"><span class="mark"></span>BrookSpan</div>
    <div class="badge grey" style="left:72px;top:178px;width:70px;height:42px"></div>
    <div class="badge pink" style="left:158px;top:178px;width:70px;height:42px"></div>
    <p class="fineprint" style="left:0;right:0;top:380px;text-align:center">Company Name Limited · Street Address Line · City, Region, Country<br>mail@company.example · +000 (0) 0000000</p>
  </section>
  <p class="label" style="left:573px;top:427px">Letter Head Option 2</p>

  <div class="sheet envelope-dark" role="img" aria-label="Black envelope back with closed flap"></div>
  <div class="sheet envelope-red" role="img" aria-label="Dark red envelope flap"></div>
  <section class="sheet envelope-flap">
    <div class="wordmark"><span class="mark"></span>BrookSpan</div>
  </section>
  <section class="sheet envelope-front">
    <div class="top-band"></div>
    <div class="wordmark"><span class="mark"></span>BrookSpan</div>
  </section>
  <p class="label" style="left:1012px;top:400px">Envelope Option 2</p>
</body>
</html>
```